QV - menu design

Hi,

We require elegant menu design for upscale restaurant. Please find attached the logo and the menu items for your reference.

for inspiration, this is a good website: -
http://www.platewhisper.example/bellfoldnotes/about.php

We are very much open for Menu Size suggestions.

unfortunately the place is going under renovation, we don't have updated images to it. the closest look and feel to our place is http://varnelo.example ..

we are also open for creative options on the shape, the styles, etc. as long as it represents the fine dine feel ...

Thanks ...

Dear All,

We wouldlike to extend our apology for not being able to provide feedbacks on everysingle design. We were extremely busy and we have multiple contests opensimultaneously which makes the process even harder.

However,we would like to thank you all for the efforts you have put into designingour menu. It is very much appreciated …

We wishyou all success in your design ventures and we are quite positive that we willbe working with many of you on many projects in the soon future. 

Thanks & Regards,

TLG Team...

 

 

 

Industry/Entity Type

Restaurant

Requirements
Must have
• Please ensure that there are 'some' images in the menu ... this is very important.
Should not have
• IMPORTANT: -

1. Please DO NOT insert any currency sign to the menu
2. Please keep the prices of the menu at the end of the menu items descriptions NOT beside the menu item names. The font of the price should be similar to the menu item description and please DO NOT bold the numbers. the prices should be subtle.

Thank you ...

```html
<!DOCTYPE html>
<html lang="en">
<head>
<meta charset="utf-8">
<title>QV – The Breakfast Menu</title>
<link rel="stylesheet" href="https://fonts.googleapis.com/css2?family=Anton&family=Roboto+Condensed:ital,wght@1,400;1,700&display=swap">
<style>
  :root {
    --backdrop: #e4e4e4;
    --page-dark: #1d1a1d;
    --earth: #8a7050;
    --band-green: #24573a;
    --band-grey: #4f5457;
    --photo-light: #e8e6e3;
    --photo-mid: #c9c5bf;
    --text-light: #ffffff;
  }
  * { box-sizing: border-box; margin: 0; padding: 0; }
  html, body { width: 1200px; height: 900px; overflow: hidden; }
  body {
    background: var(--backdrop);
    font-family: "Roboto Condensed", "Arial Narrow", sans-serif;
  }
  .menu-spread {
    position: absolute;
    left: 200px; top: 50px;
    width: 800px; height: 800px;
    display: flex;
    box-shadow: 0 10px 30px rgba(0,0,0,0.18);
  }
  .cover-page {
    position: relative;
    width: 400px; height: 800px;
    background: var(--earth);
    overflow: hidden;
  }
  .cover-photo {
    position: absolute; left: 0; top: 0;
    width: 400px; height: 560px;
    background: radial-gradient(ellipse at 55% 40%, var(--photo-light) 0%, var(--photo-mid) 70%, #a9a49d 100%);
  }
  .corner-triangle {
    position: absolute; left: 0; top: 0;
    width: 70px; height: 200px;
  }
  .zigzag-edge {
    position: absolute; left: 0; top: 542px;
    width: 400px; height: 26px;
  }
  .cover-title {
    position: absolute; left: 30px; top: 640px;
    font-family: "Anton", "Impact", sans-serif;
    font-size: 56px; line-height: 1;
    color: var(--text-light);
    letter-spacing: 0.5px;
  }
  .brand-mark {
    position: absolute; left: 32px; top: 745px;
    display: flex; align-items: center; gap: 6px;
  }
  .brand-mark__square {
    width: 10px; height: 10px; background: var(--text-light);
  }
  .brand-mark__name {
    font-family: "Anton", "Impact", sans-serif;
    font-size: 16px; color: var(--text-light); letter-spacing: 1px;
  }
  .items-page {
    position: relative;
    width: 400px; height: 800px;
    background: var(--page-dark);
    color: var(--text-light);
    overflow: hidden;
  }
  .band { position: absolute; left: 0; width: 400px; height: 26px; }
  .band--green { top: 30px; background: var(--band-green); }
  .band--grey { top: 82px; background: var(--band-grey); }
  .menu-list {
    position: absolute; left: 42px; top: 150px; width: 320px;
    list-style: none;
  }
  .menu-item { margin-bottom: 30px; }
  .menu-item__name {
    font-weight: 700; font-style: italic;
    font-size: 14px; letter-spacing: 0.6px;
    margin-bottom: 12px;
  }
  .menu-item__desc {
    font-style: italic; font-weight: 400;
    font-size: 10.5px; line-height: 1.35;
  }
</style>
</head>
<body>
  <main class="menu-spread">
    <section class="cover-page">
      <div class="cover-photo" role="img" aria-label="Fashion portrait of a woman with curly blonde hair in a black dress, arms raised, on a light grey studio backdrop"></div>
      <svg class="corner-triangle" viewBox="0 0 70 200" preserveAspectRatio="none" aria-hidden="true">
        <polygon points="0,0 70,0 0,200" fill="#1d1a1d"/>
      </svg>
      <svg class="zigzag-edge" viewBox="0 0 400 26" preserveAspectRatio="none" aria-hidden="true">
        <polygon fill="#8a7050" points="0,26 12.5,0 25,26 37.5,0 50,26 62.5,0 75,26 87.5,0 100,26 112.5,0 125,26 137.5,0 150,26 162.5,0 175,26 187.5,0 200,26 212.5,0 225,26 237.5,0 250,26 262.5,0 275,26 287.5,0 300,26 312.5,0 325,26 337.5,0 350,26 362.5,0 375,26 387.5,0 400,26"/>
      </svg>
      <h1 class="cover-title">The Breakfast</h1>
      <div class="brand-mark">
        <span class="brand-mark__square"></span>
        <span class="brand-mark__name">QV</span>
      </div>
    </section>

    <section class="items-page">
      <div class="band band--green"></div>
      <div class="band band--grey"></div>
      <ul class="menu-list">
        <li class="menu-item">
          <h2 class="menu-item__name">Butter Croissant</h2>
          <p class="menu-item__desc">Served plain with a selection of two jams,<br>a vanilla custard cream, a chocolate Cream and butter curls ). 36</p>
        </li>
        <li class="menu-item">
          <h2 class="menu-item__name">Cheese Croissant</h2>
          <p class="menu-item__desc">Crumbly freshly baked with cheese filling. 29</p>
        </li>
        <li class="menu-item">
          <h2 class="menu-item__name">Daily Fresh Eggs</h2>
          <p class="menu-item__desc">A choice of (poached, scrambled, pan fried, omelet) all served with toasted bread, mushrooms, roasted tomatoes and chicken sausages. 59</p>
        </li>
        <li class="menu-item">
          <h2 class="menu-item__name">Healthy Time</h2>
          <p class="menu-item__desc">One choice of hot beverage from our cafe served with fruit salad, natural Yoghurt, whole wheat bread vegetable sandwiches and sugar free biscuits selection 49</p>
        </li>
        <li class="menu-item">
          <h2 class="menu-item__name">Energy Time</h2>
          <p class="menu-item__desc">One choice of hot beverage from our cafe served with finger chocolate muffins, Poached egg with toasted bread and crispy beef bacon, crepe roll with goat Cheese and honey and finger chocolate cream with salted cookies. 59</p>
        </li>
        <li class="menu-item">
          <h2 class="menu-item__name">Quill Vale Time</h2>
          <p class="menu-item__desc">One choice of hot beverage from our cafe served with our selection of scones, Smoked salmon and avocado sandwich, roasted sausages sandwich, grilled vegetables sandwich, selection of our best biscuits. 59</p>
        </li>
        <li class="menu-item">
          <h2 class="menu-item__name">The Arabic Breakfast</h2>
          <p class="menu-item__desc">Choice of Zattar Manakish and Cheese Manakish, served with one choice of hot beverage from our cafe and fresh orange juice. 59</p>
        </li>
      </ul>
    </section>
  </main>
</body>
</html>
```